Flyer for annual KESTREL SUMMIT 2020

I would like a church event flyer designed. The event is called "KESTREL SUMMIT 2020". I am looking for a professional, yet catchy design that uses our brand colors and logo creatively while communicating key information of the event effectively.

1. The logo is attached in two color formats. The designer has the choice to use them as he/she want.

2. The location of the event is: Harlow Community Center, 239 Fennimore Street, Portland, ME 04117

3. Time and date of event. The designer can organize and format the date and time as he/she pleases.
Thursday December 31st @ 6:30PM
Friday January 1st @ 6:30PM
Saturday 2nd @ 6:30PM
Sunday 3rd @ 4:30PM

4. The topic of the event is "In Fire and On Fire". The designer is free to use this phrase as he/she pleases to create a good composition.

5. Speaker: Prophet Marcus Olunde (2 pictures of the speaker to choose from are attached)

6. Contact information: contact@brightmeadowfold.org - Telephone number: 207 583 2914

7. I would also like the following three words on the flyer. These words describe the focus of the event: FIRE, REVIVAL, PROPHETIC

Target Market(s)

Young adults

Font styles to use
Sans Serif

Requirements
Must have
• Logo, speaker's picture
Should not have
• cross image, church image

```html
<!DOCTYPE html>
<html lang="en">
<head>
<meta charset="utf-8">
<title>Kestrel Summit 2020 – In Fire and On Fire</title>
<link rel="stylesheet" href="https://fonts.googleapis.com/css2?family=Roboto+Condensed:wght@300;400;500;700&display=swap">
<style>
  :root {
    --orange: #e0902f;
    --band: #df8f31;
    --peach: #f1cfa3;
    --navy: #22385a;
    --ink: #1e1e22;
    --rule: #b4b4c6;
    --paper: #ffffff;
    --suit-light: #d4593a;
    --suit-dark: #a83a22;
  }
  * { margin: 0; padding: 0; box-sizing: border-box; }
  html, body { width: 851px; height: 1200px; overflow: hidden; background: var(--paper); }
  .flyer {
    position: relative;
    width: 851px;
    height: 1200px;
    background: var(--paper);
    font-family: "Roboto Condensed", "Arial Narrow", sans-serif;
    color: var(--ink);
    overflow: hidden;
  }
  .side-band {
    position: absolute; left: 0; top: 0;
    width: 270px; height: 1200px;
    background: var(--band);
  }
  .event-title { position: absolute; left: 0; top: 0; }
  .event-title text {
    font-family: "Roboto Condensed", "Arial Narrow", sans-serif;
    font-weight: 700;
    fill: var(--peach);
  }
  .speaker-photo {
    position: absolute;
    left: 0; top: 690px;
    width: 332px; height: 510px;
    background: linear-gradient(160deg, var(--suit-light) 0%, var(--suit-dark) 85%);
    clip-path: polygon(150px 40px, 205px 0, 265px 20px, 290px 110px, 300px 190px, 332px 300px, 332px 510px, 0 510px, 0 215px, 145px 180px);
  }
  .brand {
    position: absolute;
    left: 346px; top: 108px;
    display: flex; align-items: center; gap: 12px;
  }
  .brand-mark {
    width: 22px; height: 22px; border-radius: 50%;
    background: var(--orange);
  }
  .brand-name {
    font-size: 70px; font-weight: 400; line-height: 1;
    color: var(--navy); letter-spacing: 1px;
  }
  .headline { position: absolute; left: 0; top: 0; }
  .headline text { font-family: "Roboto Condensed", "Arial Narrow", sans-serif; font-weight: 300; }
  .headline .fire { fill: var(--orange); }
  .headline .joiner { fill: var(--navy); }
  .headline .focus { fill: var(--navy); font-weight: 500; }
  .rule {
    position: absolute; left: 348px; width: 404px; height: 2px;
    background: var(--rule);
  }
  .info {
    position: absolute; left: 346px;
    font-size: 21.5px; line-height: 27.5px;
  }
  .info-label {
    display: flex; align-items: center; gap: 6px;
    color: var(--orange); font-size: 22px;
  }
  .info-label svg, .phone svg { width: 18px; height: 18px; fill: var(--orange); flex: none; }
  .info-text { color: var(--ink); }
  .phone { display: flex; align-items: center; gap: 6px; }
</style>
</head>
<body>
<main class="flyer">
  <div class="side-band"></div>

  <svg class="event-title" width="270" height="900" viewBox="0 0 270 900" aria-label="KESTREL SUMMIT 2020">
    <text font-size="110" transform="translate(135 852) rotate(-90)" textLength="785" lengthAdjust="spacingAndGlyphs">KESTREL SUMMIT</text>
    <text font-size="110" text-anchor="end" transform="translate(232 67) rotate(-90)">2020</text>
  </svg>

  <div class="speaker-photo" role="img" aria-label="Portrait of speaker Prophet Marcus Olunde in an orange-red suit"></div>

  <div class="brand">
    <span class="brand-mark"></span>
    <span class="brand-name">VELDRA</span>
  </div>

  <svg class="headline" width="851" height="620" viewBox="0 0 851 620">
    <text class="fire" x="349" y="360" font-size="158" textLength="311" lengthAdjust="spacingAndGlyphs">In Fire</text>
    <text class="joiner" x="670" y="360" font-size="80" textLength="90" lengthAdjust="spacingAndGlyphs">and</text>
    <text class="fire" x="342" y="507" font-size="188" textLength="426" lengthAdjust="spacingAndGlyphs">On Fire</text>
    <text class="focus" x="348" y="585" font-size="42" textLength="414" lengthAdjust="spacingAndGlyphs">FIRE, REVIVAL, PROPHETIC</text>
  </svg>

  <div class="rule" style="top:662px"></div>

  <section class="info" style="top:673px">
    <div class="info-label">
      <svg viewBox="0 0 20 20"><path d="M10 1a9 9 0 1 0 0 18 9 9 0 0 0 0-18zm0 2.3a6.7 6.7 0 1 1 0 13.4 6.7 6.7 0 0 1 0-13.4zM9 5v6h5V9.3h-3.3V5z"/></svg>
      Time and date:
    </div>
    <div class="info-text">Thursday December 31st @ 6:30PM<br>Friday January 1st @ 6:30PM<br>Saturday 2nd @ 6:30PM<br>Sunday 3rd @ 4:30PM</div>
  </section>

  <div class="rule" style="top:820px"></div>

  <section class="info" style="top:829px">
    <div class="info-label">
      <svg viewBox="0 0 20 20"><path d="M10 1 1 9h2.5v10h13V9H19zM7 12h2.4v2.4H7zm3.6 0H13v2.4h-2.4zM7 15.6h2.4V18H7zm3.6 0H13V18h-2.4z"/></svg>
      Location:
    </div>
    <div class="info-text">Harlow Community Center, 239 Fennimore Street,<br>Portland, ME 04117</div>
  </section>

  <div class="rule" style="top:917px"></div>

  <section class="info" style="top:927px">
    <div class="info-label">
      <svg viewBox="0 0 20 20"><circle cx="10" cy="5.5" r="4.5"/><path d="M1.5 19.5c0-5 3.8-8 8.5-8s8.5 3 8.5 8z"/></svg>
      Speaker:
    </div>
    <div class="info-text" style="margin-top:4px">Prophet Marcus Olunde</div>
  </section>

  <div class="rule" style="top:995px"></div>

  <section class="info" style="top:1003px">
    <div class="info-label">
      <svg viewBox="0 0 20 20"><path d="M10 0.5a6.8 6.8 0 0 0-6.8 6.8C3.2 12.5 10 19.5 10 19.5s6.8-7 6.8-12.2A6.8 6.8 0 0 0 10 .5zm0 4a2.8 2.8 0 1 1 0 5.6 2.8 2.8 0 0 1 0-5.6z"/></svg>
      Contact:
    </div>
    <div class="info-text" style="margin-top:2px">contact@brightmeadowfold.org</div>
    <div class="info-text phone">
      <svg viewBox="0 0 20 20"><path d="M4.3 1.2 7.2 4.4 5.6 7a11 11 0 0 0 7.4 7.4l2.6-1.6 3.2 2.9-1.7 3A15.5 15.5 0 0 1 1.2 2.9z"/></svg>
      207 583 2914
    </div>
  </section>

  <div class="rule" style="top:1098px"></div>
</main>
</body>
</html>
```